Business Card Design for Event Planning Company

Create a business card for event planning company using our new logo. After I pick the design, I will need files made for 6 employees. Our company provides event design & logistics services as well as venue management. The font should be sans serif and complementary to the logo. I will need to know the name of the font selected for the final design. The phone numbers listed should be separated by "." not "-"

Address for the card
PO Box 218, Washington, DC 20019

Card One
Lorna Pettigrew
lpettigrew@galaplanora.com
202.481.7032

Card Two
Marisol Dunleavy
mdunleavy@galaplanora.com
202.416.2950

Card Three
Rebecca Vasquetti
rvasquetti@galaplanora.com
978.527.6043

Card Four
Tessa Brink
tbrink@galaplanora.com
202.458.1276

Card Five
Ada-Rose Pemberton-Nwaku
adarose@galaplanora.com
202.819.3047

Card Six
Valerie Thornbury
Valerie@galaplanora.com
202.592.8134

Target Market(s)

Corporate/Non-Profit

Industry/Entity Type

Event Planning

Contact Information for Business Card

Address for the card

Card One
Lorna Pettigrew
lpettigrew@galaplanora.com
202.481.7032

Card Two
Marisol Dunleavy
202.416.2950

Card Three
Rebecca Vasquetti
978.527.6043

Card Four
Tessa Brink
tbrink@galaplanora.com
202.458.1276

Card Five
Ada-Rose Pemberton-Nwaku
202.819.3047

Card Six
Valerie Thornbury
202.592.8134

Font styles to use
Sans Serif

Colors

Designer to choose colors to be used in the design.

Requirements
Must have
• Two-sided with logo
Should not have
• Extra colors or be too busy

```html
<!DOCTYPE html>
<html lang="en">
<head>
<meta charset="utf-8">
<title>Galaplanora Business Card</title>
<link rel="stylesheet" href="https://fonts.googleapis.com/css2?family=Open+Sans:wght@400;600;700&family=Questrial&display=swap">
<style>
  :root {
    --teal: #5aa6a4;
    --ink: #1e1e1e;
    --text: #2b2b2b;
    --card: #ffffff;
    --stage: #e9e7e4;
  }
  * { margin: 0; padding: 0; box-sizing: border-box; }
  html, body {
    width: 1200px; height: 960px; overflow: hidden;
    background: var(--stage);
  }
  .canvas { position: relative; width: 1200px; height: 960px; }
  .card {
    position: absolute;
    width: 700px; height: 400px;
    background: var(--card);
    box-shadow: 0 6px 24px rgba(0,0,0,0.12);
    overflow: hidden;
  }
  .card-front { left: 110px; top: 50px; }
  .card-back { left: 390px; top: 510px; }

  /* Brand wordmark */
  .brand {
    display: flex; align-items: center; gap: 14px;
    font-family: "Questrial", sans-serif;
    color: var(--teal);
    font-weight: 400;
    letter-spacing: 1px;
  }
  .brand-dot {
    border-radius: 50%;
    background: var(--teal);
    flex: none;
  }

  /* Front */
  .card-front .brand {
    position: absolute; left: 0; right: 0; top: 110px;
    justify-content: center;
    font-size: 68px;
  }
  .card-front .brand-dot { width: 34px; height: 34px; }
  .front-web {
    position: absolute; left: 0; right: 0; top: 240px;
    text-align: center;
    font-family: "Questrial", sans-serif;
    font-size: 21px; letter-spacing: 3.5px;
    color: var(--ink);
  }

  /* Back */
  .notch {
    position: absolute; left: -16px; top: 78px;
    width: 32px; height: 36px; border-radius: 50%;
    background: var(--ink);
  }
  .person-name {
    position: absolute; left: 40px; top: 80px;
    font-family: "Open Sans", sans-serif;
    font-weight: 700; font-size: 24px;
    color: var(--teal);
  }
  .card-back .brand {
    position: absolute; right: 36px; top: 40px;
    font-size: 46px;
  }
  .card-back .brand-dot { width: 24px; height: 24px; }
  .contact {
    position: absolute; left: 40px; top: 240px;
    font-family: "Open Sans", sans-serif;
    font-size: 16px; color: var(--text);
    list-style: none;
  }
  .contact li { display: flex; align-items: center; gap: 9px; height: 27px; }
  .contact .address { margin-top: 12px; font-size: 17px; }
  .contact svg { width: 14px; height: 14px; flex: none; }
  .web-band {
    position: absolute; right: 0; bottom: 0;
    width: 300px; height: 48px;
    background: var(--teal);
    border-radius: 26px 0 0 0;
    display: flex; align-items: center; justify-content: center;
    font-family: "Questrial", sans-serif;
    font-size: 17px; letter-spacing: 2px; color: #fff;
  }
</style>
</head>
<body>
<main class="canvas">

  <section class="card card-front" aria-label="Card front">
    <div class="brand"><span class="brand-dot"></span>galaplanora</div>
    <p class="front-web">www.galaplanora.com</p>
  </section>

  <section class="card card-back" aria-label="Card back">
    <span class="notch"></span>
    <h1 class="person-name">Lorna Pettigrew</h1>
    <div class="brand"><span class="brand-dot"></span>galaplanora</div>
    <ul class="contact">
      <li>
        <svg viewBox="0 0 14 14" aria-hidden="true"><rect x="3" y="0.5" width="8" height="13" rx="1.5" fill="none" stroke="#5aa6a4" stroke-width="1.4"/><rect x="5" y="3" width="4" height="4" fill="#5aa6a4"/><circle cx="7" cy="10.5" r="1" fill="#5aa6a4"/></svg>
        202.481.7032
      </li>
      <li>
        <svg viewBox="0 0 14 14" aria-hidden="true"><rect x="0.7" y="3" width="12.6" height="9" rx="1" fill="#5aa6a4"/><path d="M1 3.5 L7 8.5 L13 3.5" fill="none" stroke="#fff" stroke-width="1.2"/></svg>
        lpettigrew@galaplanora.com
      </li>
      <li class="address">PO Box 218, Washington, DC 20019</li>
    </ul>
    <div class="web-band">www.galaplanora.com</div>
  </section>

</main>
</body>
</html>
```